依頼詳細
『Velva Prism ヴェルヴァプリズム』のアルミ袋デザインを依頼させて頂きます。

商品サイトがありますのでこのサイトにイメージを合わせて頂けたらと思います。
商品サイト  http://velvaprism-shop.net/item/

参考画像も貼っておきます。

色数は背景含めて3色でお願いします。
希望イメージは薄いピンクで背景はグラデーションをかけて下さい。
花や葉っぱなど、上品な感じの模様を背景に少し入れて下さい。(参考画像のような柄でお願いします)
記載項目
サブタイトル: 30歳を過ぎたらフルボディケア

商品名: Velva Prism  ヴェルヴァプリズム ← ローマ字の方を大きめに目立つように記載してほしいです。

プラセンタ、コラーゲン、ヒアルロン酸、プエラリア、ローヤルゼリー、
はと麦、真珠パウダーなどあらゆる美容成分をオールインワンにしました。←下の方にいれてほしい文章です。

1袋90粒入り
希望イメージ
シンプル 複雑
単色 カラフル
暗い 明るい
日常 高級
遊び心 厳粛
未来的 伝統的
女性的 男性的
希望する色
ピンク、白等で優しく綺麗な感じでお願いします。
納品ファイル
• イラストレーター形式 (.ai)
• フォトショップ形式 (.psd)
補足説明
依頼公開後の追記内容
■ 選んだ理由

ピンクと白を使った優しく上品な感じが、こちらのイメージとぴったり
あっていましたので選ばせて頂きました。

■ 提案者全員のお礼・コメント

たくさんの提案を本当にありがとうございました。
色んなタイプがあり、とても迷いました。
今回のイメージに合う提案もたくさんあり、本当に
ありがとうございました。

```html
<!DOCTYPE html>
<html lang="ja">
<head>
<meta charset="utf-8">
<title>Velva Prism ヴェルヴァプリズム パッケージ</title>
<link rel="stylesheet" href="https://fonts.googleapis.com/css2?family=Cormorant+Garamond:wght@400;500&family=Noto+Sans+JP:wght@400;700&family=Noto+Serif+JP:wght@400&display=swap">
<style>
  :root {
    --bg: #ffffff;
    --pink-deep: #e24a85;
    --pink-mid: #ec7aa7;
    --pink-light: #f7c3d8;
    --white: #ffffff;
    --silver: #eeeef0;
    --silver-dark: #d9d9de;
    --gold: #c9a24a;
    --ink-soft: #8a8a92;
  }
  html, body { margin: 0; padding: 0; overflow: hidden; }
  body { width: 882px; height: 1200px; background: var(--bg); position: relative; }
  .pouch {
    position: absolute; left: 160px; top: 60px; width: 565px; height: 1060px;
    border-radius: 14px; overflow: hidden;
    background: linear-gradient(165deg, var(--pink-deep) 0%, var(--pink-mid) 55%, var(--pink-light) 100%);
  }
  .pouch__header {
    position: absolute; left: 0; top: 0; width: 100%; height: 110px;
    background: linear-gradient(180deg, var(--white), var(--silver));
    border-bottom: 3px solid var(--silver-dark);
  }
  .pouch__notice {
    position: absolute; left: 36px; font-family: "Noto Sans JP", sans-serif;
    font-size: 11px; color: var(--ink-soft);
  }
  .pouch__notice--cut { top: 18px; }
  .pouch__notice--zip { top: 58px; left: 200px; font-size: 10px; }
  .pouch__cutline {
    position: absolute; left: 36px; right: 36px; top: 38px;
    border-top: 1px dashed var(--silver-dark);
  }
  .pouch__marks { position: absolute; right: 36px; top: 52px; display: flex; gap: 12px; }
  .pouch__mark { width: 24px; height: 24px; border: 2px solid var(--ink-soft); border-radius: 3px; }
  .pouch__floral {
    position: absolute; right: 0; top: 140px; width: 240px; height: 420px;
    background: radial-gradient(ellipse at 60% 45%, rgba(255,255,255,0.5), rgba(255,255,255,0) 70%);
  }
  .brand {
    position: absolute; left: 40px; top: 300px; margin: 0;
    color: var(--white); font-family: "Noto Sans JP", sans-serif; font-weight: 400;
    font-size: 64px; line-height: 1; letter-spacing: 2px;
  }
  .brand-kana {
    position: absolute; left: 42px; top: 390px; margin: 0;
    font-family: "Noto Sans JP", sans-serif; font-weight: 400;
    font-size: 20px; letter-spacing: 4px; color: var(--white);
  }
  .tagline {
    position: absolute; left: 30px; right: 30px; top: 520px; height: 46px;
    background: var(--white); color: var(--pink-deep);
    font-family: "Noto Sans JP", sans-serif; font-weight: 700; font-size: 28px;
    display: flex; align-items: center; justify-content: center; letter-spacing: 1px;
  }
  .ingredients {
    position: absolute; left: 36px; top: 590px; width: 500px; margin: 0;
    font-family: "Noto Sans JP", sans-serif; font-size: 18px; line-height: 1.85; color: var(--white);
  }
  .count {
    position: absolute; left: 410px; top: 880px; width: 96px; height: 96px; border-radius: 50%;
    background: var(--white); border: 5px solid var(--gold);
    display: flex; flex-direction: column; align-items: center; justify-content: center;
    color: var(--gold); font-family: "Cormorant Garamond", serif;
  }
  .count__number { font-size: 42px; line-height: 1; }
  .count__unit { font-family: "Noto Sans JP", sans-serif; font-size: 11px; }
</style>
</head>
<body>
  <div class="pouch">
    <div class="pouch__header">
      <span class="pouch__notice pouch__notice--cut">✂ ここから切り取ってください</span>
      <div class="pouch__cutline"></div>
      <span class="pouch__notice pouch__notice--zip">開封後はチャックを閉めて保管</span>
      <div class="pouch__marks"><span class="pouch__mark"></span><span class="pouch__mark"></span></div>
    </div>
    <div class="pouch__floral" role="img" aria-label="淡いピンクの花と葉のシルエット模様"></div>
    <p class="brand">Velva Prism</p>
    <p class="brand-kana">ヴェルヴァプリズム</p>
    <div class="tagline">30歳を過ぎたらフルボディケア</div>
    <p class="ingredients">プラセンタ、コラーゲン、ヒアルロン酸、ローヤルゼリー、<br>プエラリア、はと麦、真珠パウダーなどあらゆる<br>■美容成分をオールインワンにしました。</p>
    <div class="count"><span class="count__number">90</span><span class="count__unit">粒入り</span></div>
  </div>
</body>
</html>
```